Locksmith business card design

i need a business card design for a new locksmith/auto Locksmith company we cater for residental/commercial/industrial/vehicles locksmithing we provide a 24/7 emergency service we are fully insured and certified i like the idea of black with white writing i would like the final design to communicate we are very affordable compared to our competitors

Target Market(s)

everyone

Industry/Entity Type

Business

Contact Information for Business Card

Brenton's 24h Locksmiths, Owen Brenton, 27 marsh lane colby ferris pk428tw, brentons_locksmiths@quillmail.test,07724619038,www.brentonslocksmith.test

Requirements
Must have
• some sort of logo/picture

```html
<!DOCTYPE html>
<html lang="en">
<head>
<meta charset="utf-8">
<title>Brenton's 24h Locksmiths – Business Card</title>
<link rel="stylesheet" href="https://fonts.googleapis.com/css2?family=Tinos&display=swap">
<style>
  :root {
    --card-black: #08090a;
    --ink-white: #ffffff;
  }
  html, body {
    margin: 0;
    padding: 0;
    width: 1200px;
    height: 791px;
    overflow: hidden;
    background: var(--card-black);
  }
  .business-card {
    position: relative;
    width: 1200px;
    height: 791px;
    background: var(--card-black);
    overflow: hidden;
  }
  .contact-block {
    position: absolute;
    left: 151px;
    top: 232px;
    height: 325px;
    border-left: 2px solid var(--ink-white);
    padding-left: 27px;
    box-sizing: border-box;
    font-family: "Tinos", "Times New Roman", serif;
    font-size: 35px;
    color: var(--ink-white);
  }
  .contact-line {
    margin: 0;
    height: 62.5px;
    line-height: 62.5px;
    white-space: nowrap;
  }
  .contact-line:first-child { margin-top: 4px; }
  .vehicle-illustration {
    position: absolute;
    left: 583px;
    top: 658px;
    width: 590px;
    height: 92px;
  }
  .ground-band {
    position: absolute;
    left: 0;
    bottom: 0;
    width: 1200px;
    height: 43px;
    background: var(--ink-white);
  }
</style>
</head>
<body>
  <main class="business-card">
    <section class="contact-block">
      <p class="contact-line company-name">Brenton's 24h Locksmiths</p>
      <p class="contact-line owner-address">Owen Brenton, 27 marsh lane colby ferris pk428tw</p>
      <p class="contact-line email">Email : brentons_locksmiths@quillmail.test</p>
      <p class="contact-line phone">Phone : 07724619038</p>
      <p class="contact-line website">Website : www.brentonslocksmith.test</p>
    </section>
    <svg class="vehicle-illustration" viewBox="0 0 590 92" role="img" aria-label="White silhouette of a speeding car along the bottom edge">
      <rect x="0" y="0" width="590" height="92" rx="40" ry="40" fill="#ffffff"/>
    </svg>
    <div class="ground-band"></div>
  </main>
</body>
</html>
```